Business card design for industrial spray painting - startup business

Design the layout of our new business card using the logo we have provided.

We want the card to be matt black in colour.

We only want our logo and slogan on the face side.

Because the card is black we would like the slogan WE PAINT ANYTHING! to be in white.

We want our information on the rear side.

I would like my name in blue matching the blue in the logo.

The remainder of the information should be in grey to match the grey in the logo.

The overall finish should look minimal, clean and slick.

Our business is industrlal and of a masculine nature.

Target Market(s)

industrial and mining companies

Contact Information for Business Card

(front of card – matt black)
insert logo here:
insert this tag line: WE PAINT ANYTHING!

--------------------------------------------------------------------------------------------------------------

(back of card – matt black)
Dorian Pelkey
Paint and Coatings Specialist
47 Holloway Crescent, Kenwick WA 6107
M: +61 431 872 914
T: +61 8 555 7136
E: dorian@gleamcoat.co
W: www.gleamcoat.co

Font styles to use
Sans Serif

Colors
000000
0455a3

Requirements
Must have
• clean, slick minimalist look. Masculine as we deal mostly with industrial spray painting

```html
<!DOCTYPE html>
<html lang="en">
<head>
<meta charset="utf-8">
<title>Gleamcoat Business Card</title>
<link rel="stylesheet" href="https://fonts.googleapis.com/css2?family=Montserrat:wght@700&family=Roboto+Condensed:wght@400&family=Michroma&display=swap">
<style>
  :root {
    --backdrop: #7d7d7d;
    --card: #000000;
    --brand-blue: #1a6fbd;
    --name-blue: #0f5fae;
    --brand-grey: #8a8a8c;
    --text-grey: #9a9a9a;
    --white: #ffffff;
  }
  html, body {
    margin: 0;
    width: 1200px;
    height: 1200px;
    overflow: hidden;
    background: var(--backdrop);
  }
  .card {
    position: absolute;
    left: 241px;
    width: 719px;
    height: 421px;
    background: var(--card);
  }
  .card--front { top: 138px; }
  .card--back { top: 624px; }

  .brand {
    position: absolute;
    left: 0;
    right: 0;
    display: flex;
    justify-content: center;
    align-items: center;
    gap: 16px;
    font-family: "Michroma", sans-serif;
    font-size: 38px;
    letter-spacing: 2px;
    color: var(--brand-blue);
  }
  .brand__square {
    width: 26px;
    height: 26px;
    background: var(--brand-blue);
  }
  .card--front .brand { top: 186px; }
  .card--back .brand { top: 96px; }

  .slogan {
    position: absolute;
    left: 0;
    right: 0;
    top: 366px;
    text-align: center;
    font-family: "Montserrat", sans-serif;
    font-weight: 700;
    font-size: 21px;
    letter-spacing: 0.5px;
    color: var(--white);
  }

  .person {
    position: absolute;
    left: 131px;
    top: 254px;
    font-family: "Roboto Condensed", sans-serif;
  }
  .person__name {
    margin: 0;
    font-size: 25px;
    font-weight: 400;
    color: var(--name-blue);
    text-transform: uppercase;
    line-height: 1.1;
  }
  .person__role {
    margin: 2px 0 0;
    font-size: 18px;
    color: var(--text-grey);
  }

  .divider {
    position: absolute;
    left: 359px;
    top: 216px;
    width: 2px;
    height: 140px;
    background: var(--name-blue);
  }

  .contact {
    position: absolute;
    left: 387px;
    top: 214px;
    font-family: "Roboto Condensed", sans-serif;
    font-size: 18px;
    color: var(--text-grey);
    line-height: 21px;
  }
  .contact__address { margin: 0 0 14px; }
  .contact__list { list-style: none; margin: 0; padding: 0; }
  .contact__item {
    display: flex;
    align-items: center;
    height: 21.5px;
  }
  .contact__icon {
    width: 12px;
    height: 12px;
    margin: 0 12px 0 6px;
    fill: var(--name-blue);
  }
</style>
</head>
<body>
  <section class="card card--front">
    <div class="brand"><span class="brand__square"></span><span class="brand__name">GLEAMCOAT</span></div>
    <p class="slogan" style="margin:0">WE PAINT ANYTHING!</p>
  </section>

  <section class="card card--back">
    <div class="brand"><span class="brand__square"></span><span class="brand__name">GLEAMCOAT</span></div>

    <div class="person">
      <h1 class="person__name">Dorian Pelkey</h1>
      <p class="person__role">Paint and Coatings Specialist</p>
    </div>

    <div class="divider"></div>

    <div class="contact">
      <p class="contact__address">47 Holloway Crescent,<br>Kenwick WA 6107</p>
      <ul class="contact__list">
        <li class="contact__item">
          <svg class="contact__icon" viewBox="0 0 12 12"><path d="M3 0h6a1 1 0 0 1 1 1v10a1 1 0 0 1-1 1H3a1 1 0 0 1-1-1V1a1 1 0 0 1 1-1zm0 1.5v8h6v-8z"/></svg>
          +61 431 872 914
        </li>
        <li class="contact__item">
          <svg class="contact__icon" viewBox="0 0 12 12"><path d="M0 2h3v9H0zM4 1h8v10H4zm1.5 2v2h5V3zm0 3.5v1h1v-1zm2 0v1h1v-1zm2 0v1h1v-1zm-4 2v1h1v-1zm2 0v1h1v-1zm2 0v1h1v-1z"/></svg>
          +61 8 555 7136
        </li>
        <li class="contact__item">
          <svg class="contact__icon" viewBox="0 0 12 12"><path d="M0 2h12v1.2L6 7 0 3.2zM0 4.6l6 3.8 6-3.8V10H0z"/></svg>
          dorian@gleamcoat.co
        </li>
        <li class="contact__item">
          <svg class="contact__icon" viewBox="0 0 12 12"><path d="M6 0a6 6 0 1 0 0 12A6 6 0 0 0 6 0zm0 1c.7 0 1.4 1.3 1.7 3.2H4.3C4.6 2.3 5.3 1 6 1zM1.2 5.2h2.9a11 11 0 0 0 0 1.6H1.2a4.8 4.8 0 0 1 0-1.6zm3.9 0h1.8a10 10 0 0 1 0 1.6H5.1a10 10 0 0 1 0-1.6zm2.8 0h2.9a4.8 4.8 0 0 1 0 1.6H7.9a11 11 0 0 0 0-1.6zM4.3 7.8h3.4C7.4 9.7 6.7 11 6 11s-1.4-1.3-1.7-3.2z"/></svg>
          www.gleamcoat.co
        </li>
      </ul>
    </div>
  </section>
</body>
</html>
```